Business Card for Tutoring Company

We need a logo/symbol for an education company, along with an attractive business card. The logo should resemble both a pi symbol and the letter T.

Dear Designers,

I am narrowing down what I am looking for. 
I want the front of the card to be primarily white, with the company name "Maple Grove Learning" positioned towards the center.  The first letter, 'T' in 'Maple' will be modified so that it resembles a Pi symbol.
My personal information will be at the bottom.  If you think it fits, the website can be strewn across the top.

As for the back of the card, it will be primarily blue.  Toward the center will be the same T/pi shape engraved into a circular disk/button/emblem shape with some border.  It should be noted that I do like shiny blue, like the blue face of a Vantor.  Underneath the logo will be white text that reads, "Making Independent Learners and Thinkers."  At the very bottom of the card in smaller white font, the website "MapleGroveLearning.com" is written.

For more clarification, see my recent attachment.

Thank you.

Winston

Industry/Entity Type

Education

Logo styles of interest
Pictorial/Combination Logo
Requirements
Must have
• LOGO:
The logo is a solid blue circle with a symbol cutout from it. The cut out should closely resemble π and be the color white.

CARD:
The front has the logo in the top left corner, with "MAPLE GROVE LEARNING" written out beside it, spanning the width of the card. " At the bottom, personal information can be placed: Name, Title, Phone, Email.
The back has the the logo centered and enlarged. The website is printed "MapleGroveLearning.com
Nice to have
• LOGO:
It would be nice if the logo/pi symbol could be used as a letter T when spelling MGL or Maple Grove Learning.

CARD:
The enlarged logo on the back of the card can be enhanced (i.e. the blue is not solid blue but shiny, like the metallic blue face of a vantor) It would also be nice if the logo had a cool background (i.e. instead of the cutout of the pi-shape being white, it could be outerspace or something. Also, a motto "Making Independent Learner and Thinkers" printed under "MapleGroveLearning.com" would be nice, if it fits.

```html
<!DOCTYPE html>
<html lang="en">
<head>
<meta charset="utf-8">
<title>Maple Grove Learning – Business Card</title>
<link rel="stylesheet" href="https://fonts.googleapis.com/css2?family=Montserrat:wght@600;700&family=Open+Sans:wght@400;700&display=swap">
<style>
  :root {
    --stage: #3b3b3b;
    --navy: #1b2583;
    --navy-deep: #0b1566;
    --navy-shine: #2a5bc4;
    --sky: #b9e2f5;
    --white: #ffffff;
  }
  * { margin: 0; padding: 0; box-sizing: border-box; }
  html, body {
    width: 1200px; height: 900px; overflow: hidden;
    background: var(--stage);
  }
  .card {
    position: absolute; top: 301px;
    width: 514px; height: 296px;
    overflow: hidden;
  }

  /* Back side */
  .card-back {
    left: 72px;
    background: radial-gradient(ellipse 60% 75% at 52% 40%, var(--white) 0%, #e6f5fc 45%, var(--sky) 100%);
  }
  .emblem {
    position: absolute; left: 176px; top: 34px;
    width: 180px; height: 180px; border-radius: 50%;
    background: var(--navy);
    display: flex; align-items: center; justify-content: center;
    text-align: center;
    font-family: "Montserrat", sans-serif; font-weight: 600;
    font-size: 19px; line-height: 1.3; color: var(--white);
    padding: 0 28px;
  }
  .back-website {
    position: absolute; left: 0; right: 0; top: 218px;
    text-align: center;
    font-family: "Open Sans", sans-serif; font-size: 13.5px;
    color: var(--navy);
  }
  .motto-band {
    position: absolute; left: 0; right: 0; bottom: 0; height: 54px;
    background: linear-gradient(90deg, var(--navy-deep) 0%, #14257f 30%, var(--navy-shine) 50%, #14257f 70%, var(--navy-deep) 100%);
    display: flex; align-items: center; justify-content: center;
  }
  .motto {
    font-family: "Montserrat", sans-serif; font-weight: 600;
    font-size: 15px; letter-spacing: 1.6px; color: var(--white);
  }

  /* Front side */
  .card-front { left: 615px; background: var(--white); }
  .brand {
    position: absolute; left: 34px; top: 30px;
    display: flex; align-items: center; gap: 12px;
  }
  .brand-dot {
    width: 84px; height: 84px; border-radius: 50%;
    background: var(--navy);
  }
  .brand-name {
    font-family: "Montserrat", sans-serif; font-weight: 600;
    font-size: 22px; color: var(--navy);
  }
  .headline {
    position: absolute; left: 49px; top: 168px;
    font-family: "Montserrat", sans-serif; font-weight: 700;
    font-size: 26.5px; letter-spacing: -0.3px; color: var(--navy);
  }
  .rule {
    position: absolute; left: 0; right: 0; top: 205px; height: 3px;
    background: var(--navy);
  }
  .contact-band {
    position: absolute; left: 0; right: 0; top: 213px; bottom: 0;
    background: linear-gradient(90deg, var(--navy-deep) 0%, #14257f 35%, var(--navy-shine) 58%, #14257f 78%, var(--navy-deep) 100%);
    font-family: "Open Sans", sans-serif; color: var(--white);
    padding: 15px 47px 0 49px;
    display: flex; justify-content: space-between;
  }
  .person-name { font-weight: 700; font-size: 18px; line-height: 1.2; }
  .person-title { font-size: 13.5px; margin-top: 4px; }
  .contact-lines { text-align: right; font-size: 13.5px; line-height: 1.6; padding-top: 1px; }
</style>
</head>
<body>
  <section class="card card-back" aria-label="Card back">
    <div class="emblem">Maple Grove Learning</div>
    <p class="back-website">MapleGroveLearning.com</p>
    <div class="motto-band"><p class="motto">MAKING INDEPENDENT LEARNER AND THINKERS</p></div>
  </section>

  <section class="card card-front" aria-label="Card front">
    <div class="brand">
      <span class="brand-dot"></span>
      <span class="brand-name">MAPLE GROVE LEARNING</span>
    </div>
    <h1 class="headline">PREMIER EDUCATION SERVICES</h1>
    <div class="rule"></div>
    <div class="contact-band">
      <div class="person">
        <p class="person-name">Winston Hale</p>
        <p class="person-title">Education Consultant</p>
      </div>
      <div class="contact-lines">
        <p>(555) 014 2387</p>
        <p>winston@MGLbest.com</p>
      </div>
    </div>
  </section>
</body>
</html>
```